Mexican Tacos Food Truck Menu

Attached is the food truck logo. Need a menu to be place next to the window. Must contain:
- logo in the header (left or centered)
- Grouping elements: Dessert, drinks, Apps, etc.
- Group elements.
- main descrition (these are examples) Spaguetti, Pastor, etc
- Notes. Under main item for ingrediens, GF, dairy, etc.
- Price. Should be fairly visible and justify to the right
No prodiving target size but the I the design should accomodate at least two Group columns. I should be able to add or remove as needed.
Since the food truck is blue I think menu should be white based unless you have other options. I will update blue code

```html
<!DOCTYPE html>
<html lang="en">
<head>
<meta charset="UTF-8">
<title>Taquería Azul — Menu</title>
<link href="https://fonts.googleapis.com/css2?family=EB+Garamond:wght@400;500&display=swap" rel="stylesheet">
<style>
  :root{
    --navy:#0b1c5e;
    --paper:#efefef;
    --red:#ef4238;
    --yellow:#f5d235;
    --yellow-fade:rgba(245,210,53,0);
    --white:#ffffff;
    --ink:#3b3b3b;
  }
  *{margin:0;padding:0;box-sizing:border-box}
  html,body{width:910px;height:1200px;overflow:hidden;background:var(--navy)}
  .canvas{position:relative;width:910px;height:1200px;background:var(--navy)}
  .sheet{
    position:absolute;left:126px;top:136px;width:658px;height:928px;
    background:var(--paper);overflow:hidden;
    font-family:"EB Garamond",Garamond,Georgia,serif;color:var(--ink);
  }
  .header-band{position:absolute;left:0;top:0;width:658px;height:230px}
  .accent{position:absolute}
  .accent--left{left:-40px;top:320px;width:90px;height:320px;
    background:radial-gradient(ellipse at 20% 50%,var(--yellow) 0%,var(--yellow) 45%,var(--yellow-fade) 72%)}
  .accent--right{left:610px;top:470px;width:100px;height:300px;
    background:radial-gradient(ellipse at 80% 50%,var(--yellow) 0%,var(--yellow) 45%,var(--yellow-fade) 72%)}
  .accent--bottom-left{left:-60px;top:800px;width:230px;height:200px;
    background:radial-gradient(ellipse at 25% 80%,var(--yellow) 0%,var(--yellow) 45%,var(--yellow-fade) 70%)}
  .accent--bottom-right{left:488px;top:800px;width:230px;height:200px;
    background:radial-gradient(ellipse at 75% 80%,var(--yellow) 0%,var(--yellow) 45%,var(--yellow-fade) 70%)}
  .brand{
    position:absolute;left:27px;top:66px;width:160px;text-align:center;
    font-size:27px;line-height:1.05;font-weight:500;color:var(--red);
  }
  .title{
    position:absolute;left:396px;top:52px;
    font-size:66px;font-weight:400;color:var(--white);letter-spacing:1px;line-height:1;
  }
  .column{position:absolute;top:0;width:265px;height:100%}
  .column--left{left:47px}
  .column--right{left:346px}
  .group{position:absolute;left:0;width:100%}
  .group--tacos{top:242px}
  .group--drinks{top:500px}
  .group--adds{top:683px}
  .group--dessert{top:820px}
  .group-title{
    font-size:37px;font-weight:400;color:var(--red);line-height:40px;height:40px;margin-bottom:6px;
  }
  .item{margin-bottom:10px}
  .item-row{display:flex;align-items:baseline;font-size:13.5px;line-height:16px;letter-spacing:.3px}
  .item-name{white-space:nowrap}
  .item-leader{flex:1;margin:0 4px 0 14px;border-bottom:1.5px dotted var(--ink);transform:translateY(-3px)}
  .item-price{white-space:nowrap}
  .item-note{font-size:10px;line-height:12.5px;width:182px;margin-top:1px}
  .item-note--wide{width:200px}
</style>
</head>
<body>
<div class="canvas">
  <div class="sheet">
    <svg class="header-band" viewBox="0 0 658 230" aria-hidden="true">
      <path fill="var(--red)" d="M0 0 H658 V228 Q430 150 0 200 Z"/>
      <circle cx="107" cy="92" r="118" fill="var(--white)"/>
    </svg>

    <div class="accent accent--left" role="img" aria-label="Yellow paint splash decoration"></div>
    <div class="accent accent--right" role="img" aria-label="Yellow paint splash decoration"></div>
    <div class="accent accent--bottom-left" role="img" aria-label="Yellow paint splash decoration"></div>
    <div class="accent accent--bottom-right" role="img" aria-label="Yellow paint splash decoration"></div>

    <div class="brand">Taquería<br>Azul</div>
    <h1 class="title">MENU</h1>

    <div class="column column--left">
      <section class="group group--tacos">
        <h2 class="group-title">Tacos</h2>
        <div class="item"><div class="item-row"><span class="item-name">PASTOR</span><span class="item-leader"></span><span class="item-price">$12.50</span></div><p class="item-note">(marinated pork, onion, cilantro and pineapple in CORN tortilla)</p></div>
        <div class="item"><div class="item-row"><span class="item-name">DIRTY PASTOR</span><span class="item-leader"></span><span class="item-price">$12.50</span></div><p class="item-note">(marinated pork, onion, cilantro and pineapple in CORN tortilla)</p></div>
        <div class="item"><div class="item-row"><span class="item-name">1/2 GRINGA</span><span class="item-leader"></span><span class="item-price">$12.50</span></div><p class="item-note">(marinated pork, cheese, onion, cilantro and pineapple in FLOUR tortilla)</p></div>
        <div class="item"><div class="item-row"><span class="item-name">VOLCANO</span><span class="item-leader"></span><span class="item-price">$12.50</span></div><p class="item-note item-note--wide">(marinated pork, cheese in rosted CORN tortilla called tostada)</p></div>
      </section>
      <section class="group group--drinks">
        <h2 class="group-title">Drinks</h2>
        <div class="item"><div class="item-row"><span class="item-name">HORCHATA</span><span class="item-leader"></span><span class="item-price">$12.50</span></div><p class="item-note item-note--wide">(diary, good for pastor tacos and better if you went for hot salsa)</p></div>
        <div class="item"><div class="item-row"><span class="item-name">JAMAICA</span><span class="item-leader"></span><span class="item-price">$12.50</span></div><p class="item-note">(hibiscus, very refreshing)</p></div>
        <div class="item"><div class="item-row"><span class="item-name">SODAS</span><span class="item-leader"></span><span class="item-price">$12.50</span></div><p class="item-note">(hibiscus, very refreshing)</p></div>
      </section>
      <section class="group group--adds">
        <h2 class="group-title">Adds</h2>
        <div class="item"><div class="item-row"><span class="item-name">GUACAMOLE (hot or mild)</span><span class="item-leader"></span><span class="item-price">$12.50</span></div><p class="item-note">(avocado, cilantro, onion, tomato)</p></div>
        <div class="item"><div class="item-row"><span class="item-name">PICO DE GALLO</span><span class="item-leader"></span><span class="item-price">$12.50</span></div><p class="item-note">(avocado, cilantro, onion, tomato)</p></div>
      </section>
      <section class="group group--dessert">
        <h2 class="group-title">Dessert</h2>
        <div class="item"><div class="item-row"><span class="item-name">FLAN</span><span class="item-leader"></span><span class="item-price">$12.50</span></div><p class="item-note">(Eggs, dairy, high calories)</p></div>
      </section>
    </div>

    <div class="column column--right">
      <section class="group group--tacos">
        <h2 class="group-title">Tacos</h2>
        <div class="item"><div class="item-row"><span class="item-name">PASTOR</span><span class="item-leader"></span><span class="item-price">$12.50</span></div><p class="item-note">(marinated pork, onion, cilantro and pineapple in CORN tortilla)</p></div>
        <div class="item"><div class="item-row"><span class="item-name">DIRTY PASTOR</span><span class="item-leader"></span><span class="item-price">$12.50</span></div><p class="item-note">(marinated pork, onion, cilantro and pineapple in CORN tortilla)</p></div>
        <div class="item"><div class="item-row"><span class="item-name">1/2 GRINGA</span><span class="item-leader"></span><span class="item-price">$12.50</span></div><p class="item-note">(marinated pork, cheese, onion, cilantro and pineapple in FLOUR tortilla)</p></div>
        <div class="item"><div class="item-row"><span class="item-name">VOLCANO</span><span class="item-leader"></span><span class="item-price">$12.50</span></div><p class="item-note item-note--wide">(marinated pork, cheese in rosted CORN tortilla called tostada)</p></div>
      </section>
      <section class="group group--drinks">
        <h2 class="group-title">Drinks</h2>
        <div class="item"><div class="item-row"><span class="item-name">HORCHATA</span><span class="item-leader"></span><span class="item-price">$12.50</span></div><p class="item-note item-note--wide">(diary, good for pastor tacos and better if you went for hot salsa)</p></div>
        <div class="item"><div class="item-row"><span class="item-name">JAMAICA</span><span class="item-leader"></span><span class="item-price">$12.50</span></div><p class="item-note">(hibiscus, very refreshing)</p></div>
        <div class="item"><div class="item-row"><span class="item-name">SODAS</span><span class="item-leader"></span><span class="item-price">$12.50</span></div><p class="item-note">(hibiscus, very refreshing)</p></div>
      </section>
      <section class="group group--adds">
        <h2 class="group-title">Adds</h2>
        <div class="item"><div class="item-row"><span class="item-name">GUACAMOLE (hot or mild)</span><span class="item-leader"></span><span class="item-price">$12.50</span></div><p class="item-note">(avocado, cilantro, onion, tomato)</p></div>
        <div class="item"><div class="item-row"><span class="item-name">PICO DE GALLO</span><span class="item-leader"></span><span class="item-price">$12.50</span></div><p class="item-note">(avocado, cilantro, onion, tomato)</p></div>
      </section>
      <section class="group group--dessert">
        <h2 class="group-title">Dessert</h2>
        <div class="item"><div class="item-row"><span class="item-name">FLAN</span><span class="item-leader"></span><span class="item-price">$12.50</span></div><p class="item-note">(Eggs, dairy, high calories)</p></div>
      </section>
    </div>
  </div>
</div>
</body>
</html>
```